Web Design Project

To develop a web based Council Meeting Support system which includes 2 major components for each Council member:
1. Allow a council member to Vote on a motion during a council session
2. Allow a council member to flag notify the Chair their intention to speak on a motion
The application will have 3 separate interfaces:
Chair interface: Allows the Chair of the session to review voting and manage the speaker queue
Council interface: Allows each council member to vote on each motion and add flag their intention to speak for or against a motion
Admin interface: Allows administrators to initiate a session and import details on all meeting participants
We will begin by designing the Council Interface. (An example wireframe is attached) This council interface will give members the ability to request to speak, vote, view voting results and viewing the current motion number.
*** 4 Designs will be required overall. One for each interface and a login page ***
Needs to be designed so that it works well on an Tavlo or any tablet device.
Update: Looking for a brighter design, not a dark grey one. The blue colour from qarvel.example would be good.
- Request to Speak
Voting
Vote Results
Current Motion Number

```html
<!DOCTYPE html>
<html lang="en">
<head>
<meta charset="utf-8">
<title>Council Meeting Support – Member Screens</title>
<link rel="stylesheet" href="https://fonts.googleapis.com/css2?family=Arimo:wght@400;700&display=swap">
<style>
  :root {
    --page-bg: #eef1f4;
    --screen-bg: #ffffff;
    --brand-blue: #2a63c9;
    --band-top: #4aabd3;
    --band-bottom: #3893bd;
    --rule: #e2e2e2;
    --heading: #333333;
    --body: #555555;
    --accent-blue: #3aa0cc;
    --subhead: #4a5a6a;
    --for-bg: #e0fde0;
    --against-bg: #fde0de;
    --bar: #d6d6d6;
    --nav: #333333;
  }
  * { box-sizing: border-box; margin: 0; padding: 0; }
  html, body { width: 1200px; height: 750px; overflow: hidden; }
  body {
    background: var(--page-bg);
    font-family: "Arimo", Arial, sans-serif;
    position: relative;
  }
  .screen {
    position: absolute;
    top: 102px;
    width: 365px;
    height: 546px;
    background: var(--screen-bg);
    box-shadow: 0 4px 18px rgba(0, 0, 0, 0.12);
    overflow: hidden;
  }
  .screen--speak { left: 190px; }
  .screen--results { left: 645px; }

  /* Speak screen */
  .site-header { position: absolute; top: 0; left: 0; width: 100%; height: 100px; border-bottom: 1px solid var(--rule); }
  .brand { position: absolute; top: 30px; left: 0; width: 100%; display: flex; justify-content: center; align-items: center; gap: 10px; }
  .brand__mark { width: 22px; height: 22px; background: var(--brand-blue); }
  .brand__name { font-size: 22px; font-weight: 700; color: var(--brand-blue); letter-spacing: -0.2px; }
  .site-nav { position: absolute; top: 78px; width: 100%; text-align: center; font-size: 11px; font-weight: 700; color: var(--nav); word-spacing: 4px; }
  .motion-band {
    position: absolute; top: 105px; left: 0; width: 100%; height: 100px;
    background: linear-gradient(var(--band-top), var(--band-bottom));
    border-bottom: 1px solid #2f86ae;
  }
  .motion-band__title { position: absolute; top: 30px; left: 46px; color: #fff; font-size: 19px; font-weight: 700; text-shadow: 0 1px 1px rgba(0,0,0,0.25); }
  .band-rule { position: absolute; top: 210px; left: 0; width: 100%; height: 1px; background: var(--rule); }
  .section-title { position: absolute; left: 46px; font-size: 15px; font-weight: 700; color: var(--heading); }
  .section-title--speak { top: 247px; }
  .section-rule { position: absolute; left: 46px; height: 1px; background: var(--rule); }
  .section-rule--speak { top: 275px; width: 275px; }
  .speak-option { position: absolute; left: 46px; display: flex; align-items: center; gap: 12px; }
  .speak-option svg { width: 48px; height: 48px; }
  .speak-option__title { font-size: 15px; font-weight: 700; color: var(--heading); }
  .speak-option__title--active { color: var(--accent-blue); }
  .speak-option__sub { font-size: 9.5px; color: var(--subhead); margin-top: 4px; text-transform: uppercase; }
  .speak-option--for { top: 312px; }
  .speak-option--against { top: 382px; }
  .speak-option--remove { top: 451px; }

  /* Results screen */
  .section-title--results { top: 15px; left: 40px; }
  .section-rule--results { top: 43px; left: 40px; width: 280px; }
  .vote-card { position: absolute; left: 40px; width: 281px; }
  .vote-card svg { position: absolute; top: 0; left: 0; }
  .vote-card--for { top: 67px; height: 254px; }
  .vote-card--against { top: 331px; height: 211px; }
  .vote-card__head { position: absolute; top: 8px; left: 33px; right: 33px; display: flex; align-items: center; gap: 10px; font-size: 12px; font-weight: 700; color: var(--heading); }
  .vote-card__head::after { content: ""; flex: 1; height: 4px; background: var(--bar); }
  .vote-list { position: absolute; top: 46px; left: 33px; list-style: none; }
  .vote-list li { font-size: 12px; line-height: 21.4px; color: var(--body); }
  .vote-list li::before { content: "»"; font-size: 10px; color: #888; margin-right: 11px; }
</style>
</head>
<body>

<section class="screen screen--speak">
  <header class="site-header">
    <div class="brand"><span class="brand__mark"></span><span class="brand__name">Qarvel Engineers</span></div>
    <nav class="site-nav">Home Help Logout</nav>
  </header>
  <div class="motion-band"><h1 class="motion-band__title">Current Motion # : 541</h1></div>
  <div class="band-rule"></div>

  <h2 class="section-title section-title--speak">I would like to Speak :</h2>
  <div class="section-rule section-rule--speak"></div>

  <div class="speak-option speak-option--for">
    <svg viewBox="0 0 48 48" aria-hidden="true">
      <circle cx="24" cy="24" r="23" fill="#56b4dc"/>
      <circle cx="24" cy="24" r="17" fill="#3cb843" stroke="#fff" stroke-width="2"/>
      <path d="M15 24 l6 6 l12 -12" fill="none" stroke="#fff" stroke-width="4.5" stroke-linecap="round" stroke-linejoin="round"/>
    </svg>
    <div><div class="speak-option__title speak-option__title--active">For Motion</div><div class="speak-option__sub">Subhead goes here</div></div>
  </div>

  <div class="speak-option speak-option--against">
    <svg viewBox="0 0 48 48" aria-hidden="true">
      <circle cx="24" cy="24" r="23" fill="#8a8a8a"/>
      <circle cx="24" cy="24" r="17" fill="#e02a2a" stroke="#fff" stroke-width="2"/>
      <path d="M17 17 L31 31 M31 17 L17 31" stroke="#fff" stroke-width="4.5" stroke-linecap="round"/>
    </svg>
    <div><div class="speak-option__title">Against Motion</div><div class="speak-option__sub">Subhead goes here</div></div>
  </div>

  <div class="speak-option speak-option--remove">
    <svg viewBox="0 0 48 48" aria-hidden="true">
      <circle cx="24" cy="24" r="23" fill="#8a8a8a"/>
      <circle cx="24" cy="24" r="17" fill="#a8a8a8" stroke="#fff" stroke-width="2"/>
      <path d="M24 14 L24 27" stroke="#fff" stroke-width="4.5" stroke-linecap="round"/>
      <circle cx="24" cy="33" r="2.6" fill="#fff"/>
    </svg>
    <div><div class="speak-option__title">Remove From Queue</div><div class="speak-option__sub">Subhead goes here</div></div>
  </div>
</section>

<section class="screen screen--results">
  <h2 class="section-title section-title--results">Voting Results :</h2>
  <div class="section-rule section-rule--results"></div>

  <div class="vote-card vote-card--for">
    <svg width="281" height="254" viewBox="0 0 281 254" aria-hidden="true">
      <polygon points="0,0 281,0 281,222 140.5,254 0,222" fill="var(--for-bg)"/>
    </svg>
    <div class="vote-card__head">For</div>
    <ul class="vote-list">
      <li>A. Marlow</li><li>D. Renshi</li><li>L. Varga</li><li>SA. Dorin</li>
      <li>P. Lindqvist</li><li>B. Marlow</li><li>R. Okafor</li><li>S. Pellam</li>
    </ul>
  </div>

  <div class="vote-card vote-card--against">
    <svg width="281" height="211" viewBox="0 0 281 211" aria-hidden="true">
      <polygon points="0,0 281,0 281,180 140.5,211 0,180" fill="var(--against-bg)"/>
    </svg>
    <div class="vote-card__head">Against</div>
    <ul class="vote-list">
      <li>P. Lindqvist</li><li>B. Marlow</li><li>R. Okafor</li>
      <li>S. Pellam</li><li>A. Marlow</li><li>D. Renshi</li>
    </ul>
  </div>
</section>

</body>
</html>
```